Plumbing Business Letterhead Design

Need a letterhead designed to use for my invoices and letters. I would like it to incorporate my business logo, which i will upload, and use light blue and grey colours. Or any colours that will work well with my logo (im not very good with art to know) . Also the letterhead needs to include the following:
Address - P.O Box 4862 Bega NSW 2550
Email - marcus@tfelwoodplumbing.com.au
ABN - 41 906 572 384
Licence No. - 582064K
Mobile - 0471286540

Plumbing

Sans Serif

```html
<!DOCTYPE html>
<html lang="en">
<head>
<meta charset="utf-8">
<title>Marcus Tfelwood Plumbing – Letterhead</title>
<link rel="stylesheet" href="https://fonts.googleapis.com/css2?family=Arimo&family=Noto+Serif&family=PT+Sans&family=Roboto+Condensed:wght@500&display=swap">
<style>
  :root {
    --paper: #ffffff;
    --ink: #333333;
    --brand-grey: #4d4f53;
    --brand-blue: #1e5a8e;
    --accent-blue: #2a8fc7;
    --rule-blue: #9fd1ec;
    --band-grey: #55575b;
    --band-orange: #f0901e;
  }
  * { margin: 0; padding: 0; box-sizing: border-box; }
  html, body { width: 939px; height: 1200px; overflow: hidden; background: var(--paper); }
  .letterhead { position: relative; width: 939px; height: 1200px; background: var(--paper); color: var(--ink); }

  .brand { position: absolute; left: 28px; top: 34px; display: flex; align-items: center; gap: 12px; }
  .brand-mark { width: 58px; height: 58px; background: var(--accent-blue); }
  .brand-name {
    font-family: "Roboto Condensed", sans-serif; font-weight: 500;
    font-size: 27px; line-height: 28px; color: var(--brand-grey); text-transform: uppercase;
  }

  .contact { position: absolute; left: 580px; top: 26px; height: 86px; border-left: 1px solid var(--rule-blue); padding-left: 20px;
    font-family: "Noto Serif", serif; font-size: 13.5px; color: var(--ink); }
  .contact p { line-height: 27px; white-space: nowrap; }
  .contact .label { color: var(--accent-blue); margin-right: 6px; }

  .greeting { position: absolute; left: 27px; top: 204px; font-family: "PT Sans", sans-serif; font-size: 17px; color: var(--brand-blue); }
  .subject { position: absolute; left: 27px; top: 254px; font-family: "Arimo", sans-serif; font-size: 17px; color: var(--brand-blue); }

  .body-text { position: absolute; left: 27px; top: 316px; width: 834px; font-family: "Arimo", sans-serif; font-size: 13.8px; line-height: 24px; text-align: justify; }
  .body-text p + p { margin-top: 22px; }

  .closing { position: absolute; left: 27px; top: 815px; font-family: "Arimo", sans-serif; font-size: 20px; color: #222; }
  .signature { position: absolute; left: 27px; top: 856px; width: 150px; height: 46px; background: linear-gradient(90deg, #e9e9e9, #f6f6f6); }

  .registration { position: absolute; left: 27px; top: 1143px; font-family: "Noto Serif", serif; font-size: 14.5px; color: var(--ink); }
  .registration span + span { margin-left: 20px; }

  .footer-band { position: absolute; left: 0; top: 1179px; width: 939px; height: 21px; }
</style>
</head>
<body>
<main class="letterhead">
  <header>
    <div class="brand">
      <div class="brand-mark"></div>
      <div class="brand-name">Marcus Tfelwood<br>Plumbing</div>
    </div>
    <address class="contact">
      <p><span class="label">C:</span>047 128 6540</p>
      <p><span class="label">E:</span>marcus@tfelwoodplumbing.com.au</p>
      <p><span class="label">A:</span>P.O Box 4862 Bega, NSW 2550</p>
    </address>
  </header>

  <p class="greeting">Hello Sir,</p>
  <h2 class="subject" style="font-weight:400">Lorem ipsum dolor sit amet, consectetuer adipiscing elit, sed diam nonummy nibh</h2>

  <section class="body-text">
    <p>Lorem ipsum dolor sit amet, consectetuer adipiscing elit, sed diam nonummy nibh euismod tincidunt ut laoreet dolore magna aliquam erat volutpat. Ut wisi enim ad minim veniam, quis nostrud exerci tation ullamcorper suscipit lobortis nisl ut aliquip ex ea commodo consequat. Duis autem vel eum iriure dolor in hendrerit in vulputate velit esse molestie consequat, vel illum dolore eu feugiat nulla facilisis at vero eros et accumsan et iusto odio dignissim qui blandit praesent luptatum zzril delenit augue duis dolore te feugait nulla facilisi.</p>
    <p>Lorem ipsum dolor sit amet, consectetuer adipiscing elit, sed diam nonummy nibh euismod tincidunt ut laoreet dolore magna aliquam erat volutpat. Ut wisi enim ad minim veniam, quis nostrud exerci tation ullamcorper suscipit lobortis nisl ut aliquip ex ea commodo consequat. Duis autem vel eum iriure dolor in hendrerit in vulputate velit esse molestie consequat, vel illum dolore eu feugiat nulla facilisis at vero eros et accumsan et iusto odio dignissim qui blandit praesent luptatum zzril delenit augue duis dolore te feugait nulla facilisi.</p>
    <p>Lorem ipsum dolor sit amet, consectetuer adipiscing elit, sed diam nonummy nibh euismod tincidunt ut laoreet dolore magna aliquam erat volutpat. Ut wisi enim ad minim veniam, quis nostrud exerci tation ullamcorper suscipit lobortis nisl ut aliquip ex ea commodo consequat. Duis autem vel eum iriure dolor in hendrerit in vulputate velit esse molestie consequat, vel illum dolore eu feugiat nulla facilisis at vero eros et accumsan et iusto odio dignissim qui blandit praesent luptatum zzril delenit augue duis dolore te feugait nulla facilisi.</p>
  </section>

  <p class="closing">Thank you</p>
  <div class="signature" role="img" aria-label="Handwritten signature of the sender"></div>

  <footer>
    <p class="registration"><span>ABN: 41 906 572 384</span><span>Licence No.: 582064K</span></p>
    <svg class="footer-band" viewBox="0 0 939 21" preserveAspectRatio="none" aria-hidden="true">
      <polygon points="0,0 448,0 418,21 0,21" fill="var(--band-grey)"/>
      <polygon points="464,0 939,0 939,21 404,21" fill="var(--band-orange)"/>
    </svg>
  </footer>
</main>
</body>
</html>
```